Professional Single Page Website Design for Velloway Advisory

Velloway Advisory is a new business consultancy specializing in providing expert services to small businesses, primarily in the brick-and-mortar retail and food service sectors. We offer a range of services including franchise development and launch, due diligence, and construction management.

Currently, we have a basic website set up at www.vellowayadvisory.example, but we need a professional touch to enhance its design and functionality.

Project Requirements:
- Single Page Design: For now, we need a single page design that effectively showcases who we are, our services, and contact information.
- Future Expansion: The design should be flexible and scalable for future expansion to include additional pages like specific service offerings, about us, and a dedicated contact page.
- Design Aesthetic: We are looking for a modern yet professional design that aligns with our brand identity.
- Logo: We have a logo that we like, which was also sourced from Pixel Forum. The logo files are attached to this project brief.

Key Sections to Include:
- Hero Section: An engaging introduction to Velloway Advisory with a strong visual impact.
- About Us: A brief overview of who we are and our mission.
- Team: Section for the profiles of the two principals.
- Services: A clear and concise presentation of our services, including franchise development, due diligence, and construction management.
- Contact Information: Easy-to-find contact details, including a form for inquiries.
- Call to Action: Encouraging visitors to get in touch with us for consultations or further information.

Design Considerations:
- Ensure the design is responsive and mobile-friendly.
- Include high-quality images and icons that complement our services and industry.
- We do not need development services, this is only a design project.

```html
<!DOCTYPE html>
<html lang="en">
<head>
<meta charset="utf-8">
<title>Velloway Advisory</title>
<link href="https://fonts.googleapis.com/css2?family=Poppins:wght@400;500;600;700&display=swap" rel="stylesheet">
<style>
:root{
  --ink:#1f2f35;
  --ink-2:#27383f;
  --mint:#7bbfa0;
  --mint-soft:#88c4aa;
  --text:#3a4448;
  --panel:#f4f6f7;
  --white:#ffffff;
}
*{box-sizing:border-box;margin:0;padding:0}
html,body{width:1200px;height:4914px;overflow:hidden}
body{font-family:"Poppins",sans-serif;color:var(--text);background:var(--white);position:relative}
.abs{position:absolute}
.btn{position:absolute;display:flex;align-items:center;justify-content:center;background:var(--ink);color:var(--mint);font-weight:600;font-size:16px;border-radius:6px}
p{font-size:13.5px;line-height:30px;text-align:justify}

/* header */
.site-header{position:absolute;left:0;top:0;width:1200px;height:93px;background:var(--white)}
.brand{position:absolute;display:flex;align-items:center;gap:12px}
.brand-dot{flex:none;width:44px;height:44px;border-radius:50%;background:var(--mint)}
.brand-name{font-weight:600;color:var(--ink);font-size:22px;line-height:1}
.nav a{position:absolute;top:36px;font-size:16px;color:var(--ink);text-decoration:none}
.nav .active{font-weight:600;border-bottom:2px solid var(--ink);padding-bottom:3px}
.nav-cta{left:944px;top:24px;width:145px;height:46px;font-weight:500}

/* hero */
.hero{position:absolute;left:0;top:93px;width:1200px;height:550px;background:var(--ink)}
.hero-photo{position:absolute;left:460px;top:0;width:740px;height:550px;background:linear-gradient(110deg,#22343a 0%,#4b5b5f 25%,#8a8478 55%,#6b5e4e 80%,#3e3a34 100%)}
.hero-shade{position:absolute;left:0;top:0;width:800px;height:550px;background:linear-gradient(90deg,var(--ink) 55%,rgba(31,47,53,0))}
.hero h1{position:absolute;left:110px;top:108px;width:520px;font-size:31px;line-height:50px;font-weight:600;color:var(--mint)}
.hero h2{position:absolute;left:110px;top:220px;font-size:18px;font-weight:500;color:var(--white)}
.hero p{position:absolute;left:110px;top:262px;width:380px;color:#dfe6e8;font-size:13px;line-height:31px;text-align:left}
.hero-cta{left:110px;top:367px;width:155px;height:50px;background:var(--white);color:var(--ink);font-size:16px}
.hero-notch{position:absolute;left:500px;top:600px}

/* section titles */
.section-title{position:absolute;left:0;width:1200px;display:flex;justify-content:center;align-items:center;gap:10px;font-size:33px;font-weight:600;color:var(--ink)}
.section-title .mark{width:24px;height:24px;border-radius:50%;background:var(--mint)}
.section-title em{font-style:normal;color:var(--mint)}

/* about */
.about-photo{position:absolute;left:170px;top:880px;width:290px;height:290px;border-radius:70px;transform:rotate(45deg);background:linear-gradient(135deg,#2f5b4a,#5f9c80 45%,#d9d5cc)}
.about-copy{position:absolute;left:600px;top:800px;width:490px}
.about-copy h3{font-size:19px;font-weight:500;color:var(--ink);margin:12px 0 6px}

/* team */
.team{position:absolute;left:0;top:1300px;width:1200px;height:424px;background:var(--ink-2)}
.team .section-title{top:55px;color:var(--mint)}
.card{position:absolute;top:140px;width:463px;height:215px;background:var(--white);border-radius:4px}
.card-photo{position:absolute;top:150px;width:195px;height:195px;border-radius:50px;transform:rotate(45deg);background:var(--mint-soft);padding:12px}
.card-photo div{width:100%;height:100%;border-radius:42px;background:linear-gradient(135deg,#c8ccd0,#8e9aa2)}
.card .info{position:absolute;left:240px;top:18px;width:205px}
.card h4{font-size:20px;font-weight:500;color:var(--ink)}
.card .role{font-size:11px;color:var(--mint);margin:6px 0 4px}
.card p{font-size:11px;line-height:22px;text-align:left}
.card .more{font-size:11px;font-weight:600;color:var(--ink);text-decoration:underline}

/* services */
.svc-bg{position:absolute;background:var(--panel);border-radius:10px}
.svc-img{position:absolute;border-radius:10px}
.svc-copy{position:absolute;width:430px}
.svc-copy h3{font-size:22px;font-weight:500;color:var(--ink);margin-bottom:8px}
.svc-copy p{font-size:13.5px;line-height:31px;margin-bottom:30px}
.svc-copy .btn{position:relative;width:153px;height:50px}

/* contact */
.footer{position:absolute;left:0;top:4312px;width:1200px;height:602px;background:var(--ink)}
.contact-box{position:absolute;left:165px;top:4136px;width:870px;height:364px;background:var(--mint-soft);border-radius:20px}
.contact-box .section-title{width:870px;top:50px}
.contact-box p{position:absolute;left:80px;top:100px;width:710px;text-align:center;color:var(--ink);font-size:13.5px}
.field{position:absolute;top:176px;width:261px;height:53px;background:var(--white);border-radius:6px;padding:16px 18px;font-size:14px;color:var(--ink)}
.submit{left:358px;top:261px;width:153px;height:46px}

/* footer */
.foot-brand{left:110px;top:4590px;width:280px}
.foot-brand .brand-dot{width:70px;height:70px}
.foot-brand .brand-name{color:var(--white);font-size:26px;line-height:30px;width:150px}
.socials{position:absolute;left:110px;top:4716px;display:flex;gap:29px}
.socials span{width:30px;height:30px;border-radius:50%;background:var(--white)}
.foot-col{position:absolute;top:4568px}
.foot-col h5{font-size:20px;font-weight:500;color:var(--white);margin-bottom:14px}
.foot-col li{list-style:none;font-size:13.5px;color:#d8e0e2;line-height:34px;display:flex;align-items:center;gap:10px}
.foot-col .contact-line{align-items:flex-start;line-height:26px;margin-bottom:14px;font-size:13px}
.icon-dot{flex:none;width:30px;height:30px;border-radius:50%;background:var(--white);display:flex;align-items:center;justify-content:center}
.divider{position:absolute;left:110px;top:4862px;width:980px;height:1px;background:#53646a}
.copyright{position:absolute;left:0;top:4880px;width:1200px;text-align:center;font-size:14px;font-weight:600;color:var(--white)}
</style>
</head>
<body>

<header class="site-header">
  <div class="brand" style="left:110px;top:24px"><span class="brand-dot"></span><span class="brand-name">Velloway Advisory</span></div>
  <nav class="nav">
    <a class="active" style="left:492px">Home</a>
    <a style="left:592px">About Us</a>
    <a style="left:718px">Team</a>
    <a style="left:817px">Services</a>
  </nav>
  <div class="btn nav-cta">Contact Us</div>
</header>

<section class="hero">
  <div class="hero-photo" role="img" aria-label="Two business advisors reviewing documents together in an office"></div>
  <div class="hero-shade"></div>
  <h1>Building Success in Southern California</h1>
  <h2>Expertise at Every Step: From Planning to Execution</h2>
  <p>At Velloway, we blend innovative strategies with local market expertise to guide your commercial real estate ventures.</p>
  <div class="btn hero-cta">Get In Touch</div>
</section>
<svg class="hero-notch" width="200" height="90" viewBox="0 0 200 90" aria-hidden="true">
  <path d="M0 43 C50 43 55 90 100 90 C145 90 150 43 200 43 L200 0 L0 0 Z" fill="#1f2f35"/>
  <circle cx="100" cy="45" r="24" fill="#7bbfa0"/>
</svg>

<div class="section-title" style="top:725px"><span class="mark"></span>About Velloway <em>Advisory</em></div>
<div class="about-photo" role="img" aria-label="Two smiling business partners in suits"></div>
<div class="about-copy">
  <p>Welcome to Velloway Advisory, your trusted partner in navigating the complexities of the real estate and small business markets. Founded by industry veterans Rafael Moreno and Evan Tao, we specialize in providing comprehensive services tailored to the unique needs of our clients. Whether you're a franchisee, a new restaurant owner, or a commercial real estate investor, our expertise in due diligence, construction management, and investment property evaluation ensures you make informed, strategic decisions.</p>
  <h3>Mission</h3>
  <p>Itaque earum rerum hic tenetur a sapiente delectus, ut aut reiciendis voluptatibus maiores alias consequatur aut perferendis doloribus asperiores repellat.</p>
</div>
<div class="btn" style="left:600px;top:1186px;width:153px;height:51px">Read More</div>

<section class="team">
  <div class="section-title"><span class="mark"></span>Our Team</div>
  <div class="card" style="left:110px"><div class="info">
    <h4>Evan Tao</h4><div class="role">PRINCIPAL</div>
    <p>Evan Tao is a seasoned real estate expert with extensive experience in project and construction management, and a licensed real estate agent in California.</p>
    <div class="more">Read More</div></div></div>
  <div class="card-photo" style="left:122px"><div role="img" aria-label="Portrait of principal Evan Tao"></div></div>
  <div class="card" style="left:624px"><div class="info">
    <h4>Rafael Moreno</h4><div class="role">PRINCIPAL</div>
    <p>Rafael Moreno brings almost 20 years of rich experience as a real estate investor and a pivotal role at one of southern California's largest real estate management firms.</p>
    <div class="more">Read More</div></div></div>
  <div class="card-photo" style="left:636px"><div role="img" aria-label="Portrait of principal Rafael Moreno"></div></div>
</section>

<div class="section-title" style="top:1765px"><span class="mark"></span>Our <em>Services</em></div>

<div class="svc-bg" style="left:600px;top:1875px;width:490px;height:347px"></div>
<div class="svc-img" style="left:600px;top:1875px;width:440px;height:305px;background:linear-gradient(135deg,#eef1f2,#dfe5e7)" role="img" aria-label="Network of small store blocks connected by lines"></div>
<div class="svc-copy" style="left:110px;top:1865px">
  <h3>Franchise Development</h3>
  <p>At Velloway Advisory, our Franchise Development &amp; Launch service is designed to transform your successful business into a thriving franchise. We start by thoroughly evaluating your business model to determine its franchisability.</p>
  <p>Once confirmed, our team handles every aspect of the franchise setup, including legal documentation, branding, marketing strategies, operational guidelines, and franchisee recruitment.</p>
  <div class="btn">Read More</div>
</div>

<div class="svc-bg" style="left:110px;top:2310px;width:490px;height:350px"></div>
<div class="svc-img" style="left:160px;top:2315px;width:440px;height:305px;background:linear-gradient(135deg,#0f2a48,#2f5c86 50%,#b8c9d8)" role="img" aria-label="Hands at a keyboard with glowing digital network overlay"></div>
<div class="svc-copy" style="left:660px;top:2305px">
  <h3>Due Diligence Services</h3>
  <p>Velloway offers comprehensive evaluations tailored to your business needs. We meticulously assess franchise opportunities, business sales, and property transactions, identifying potential risks and liabilities to safeguard your investments.</p>
  <p>Our expert team provides actionable recommendations on deal points and offers strategic guidance throughout the entire process.</p>
  <div class="btn">Read More</div>
</div>

<div class="svc-bg" style="left:600px;top:2755px;width:490px;height:410px"></div>
<div class="svc-img" style="left:600px;top:2755px;width:440px;height:357px;background:linear-gradient(135deg,#2b4a66,#c47a2a 45%,#3a5570)" role="img" aria-label="Engineers in hard hats reviewing plans on a laptop"></div>
<div class="svc-copy" style="left:110px;top:2745px">
  <h3>Construction management</h3>
  <p>Construction Management Services oversee every aspect of your construction and development projects, from initial planning to final completion. We ensure projects stay on time and within budget, providing meticulous attention to detail and proactive problem-solving.</p>
  <p>Specializing in tenant improvements (TIs) and ground-up construction for small to mid-size commercial projects, we handle everything from permitting and contractor coordination to quality control and final inspections.</p>
  <div class="btn">Read More</div>
</div>

<div class="svc-bg" style="left:110px;top:3230px;width:490px;height:350px"></div>
<div class="svc-img" style="left:160px;top:3232px;width:440px;height:306px;background:linear-gradient(180deg,#7f9cba,#c9d3db 55%,#5c5f5c)" role="img" aria-label="Modern two-storey house at dusk"></div>
<div class="svc-copy" style="left:660px;top:3222px">
  <h3>Investment Property Evaluation</h3>
  <p>Our Investment Property Evaluation Services offer detailed analysis of potential investment properties, ensuring you have a clear understanding of their profitability and risks. We provide comprehensive evaluations for both commercial properties and all types of residential income properties.</p>
  <p>Our expert team conducts in-depth profitability forecasts and risk assessments, helping you make informed investment decisions.</p>
  <div class="btn">Read More</div>
</div>

<div class="svc-bg" style="left:600px;top:3672px;width:490px;height:408px"></div>
<div class="svc-img" style="left:600px;top:3672px;width:440px;height:358px;background:linear-gradient(135deg,#5a4a3e,#d8dadc 45%,#eef0f1)" role="img" aria-label="Hands reviewing charts on a tablet and printed reports"></div>
<div class="svc-copy" style="left:110px;top:3662px">
  <h3>Market Analysis &amp; Feasibility Studies</h3>
  <p>Our Market Analysis &amp; Feasibility Studies provide in-depth research to evaluate the viability of your real estate ventures. Whether you're considering a recent or potential purchase for owner-operator use or investment, our thorough research delivers critical insights into market trends, demand, and competitive landscape.</p>
  <p>We analyze economic factors, demographic data, and potential return on investment to ensure you have a clear understanding of the opportunities and challenges ahead.</p>
  <div class="btn">Read More</div>
</div>

<footer class="footer"></footer>

<section class="contact-box">
  <div class="section-title"><span class="mark"></span>Contact Us</div>
  <p>Discover how Velloway Advisory can support your business journey. Partner with us and experience the difference our dedication and expertise can make.</p>
  <div class="field" style="left:27px">Name</div>
  <div class="field" style="left:305px">Email</div>
  <div class="field" style="left:582px">Phone Number</div>
  <div class="btn submit">Submit</div>
</section>

<div class="brand abs foot-brand"><span class="brand-dot"></span><span class="brand-name">Velloway Advisory</span></div>
<div class="socials"><span></span><span></span><span></span><span></span></div>

<div class="foot-col" style="left:430px">
  <h5>Quick Links</h5>
  <ul>
    <li>&#10140; Home</li><li>&#10140; About</li><li>&#10140; Classes</li><li>&#10140; Testimonials</li><li>&#10140; Contact Us</li>
  </ul>
</div>
<div class="foot-col" style="left:662px">
  <h5>Help Links</h5>
  <ul>
    <li>&#10140; FAQ</li><li>&#10140; Terms of use</li><li>&#10140; Privacy Policy</li><li>&#10140; Support Links</li><li>&#10140; Conditions</li>
  </ul>
</div>
<div class="foot-col" style="left:897px">
  <h5>Contact Us</h5>
  <ul>
    <li class="contact-line"><span class="icon-dot"><svg width="14" height="16" viewBox="0 0 14 16"><path d="M7 0C3.5 0 1 2.6 1 6c0 4 6 10 6 10s6-6 6-10c0-3.4-2.5-6-6-6zm0 8.5A2.5 2.5 0 1 1 7 3.5a2.5 2.5 0 0 1 0 5z" fill="#1f2f35"/></svg></span>412 Lakeview Way<br>Southbay, CA 90000</li>
    <li class="contact-line"><span class="icon-dot"><svg width="14" height="14" viewBox="0 0 14 14"><path d="M3 1l2 3-1.5 1.5a8 8 0 0 0 5 5L10 9l3 2-1 2.5C6 13 1 8 0.5 2z" fill="#1f2f35"/></svg></span>+1 555 010 0142</li>
    <li class="contact-line"><span class="icon-dot"><svg width="14" height="10" viewBox="0 0 14 10"><rect width="14" height="10" rx="1.5" fill="#1f2f35"/><path d="M1 1l6 4.5L13 1" stroke="#fff" stroke-width="1.3" fill="none"/></svg></span>info@vellowayadvisory.example</li>
  </ul>
</div>

<div class="divider"></div>
<div class="copyright">Copyrights@2024.Velloway Advisory.All Rights Reserved</div>

</body>
</html>
```